Commercial Snow Removal services flyer

I need a flyer to advertise that my company does snow plowing and salting for commercial properties. We cover the capital region of new york.

I would like potential customers to look at this flyer and say wow!

if you have any question please dont hesitate to ask

Industry/Entity Type

Snow Removal

Font styles to use
Sans Serif

Colors

Designer to choose colors to be used in the design.

Requirements
Must have
• Company name Summit Grading And Builders
• Phone 518-462-3917
• Email summitgradingandbuilders@mailbox-example.com
• Website www.summitgradingandbuilders-example.com
• Fully insured
Nice to have
• Ice melt product we use is Frost Away.
• you do not have to use all the pictures what ever you thinks looks the best
Should not have
• No idea

```html
<!DOCTYPE html>
<html lang="en">
<head>
<meta charset="utf-8">
<title>Summit Grading And Builders – Snow Removal Flyer</title>
<link href="https://fonts.googleapis.com/css2?family=Open+Sans:wght@400;600;700;800&family=Roboto+Condensed:wght@400;700&display=swap" rel="stylesheet">
<style>
:root{
  --blue:#1a6fc0;
  --blue-dark:#0f5aa6;
  --ink:#2b2b2b;
  --grey:#555;
  --page:#ffffff;
  --bg:#e9eaec;
  --snow-a:#dfe6ee;
  --snow-b:#8e9aa8;
  --machine:#c9a23a;
}
*{box-sizing:border-box;margin:0;padding:0}
html,body{width:1200px;height:1000px;overflow:hidden}
body{background:var(--bg);font-family:"Open Sans",Arial,sans-serif;color:var(--ink);position:relative}
.page{position:absolute;top:130px;width:560px;height:740px;background:var(--page);box-shadow:0 6px 24px rgba(0,0,0,.18);overflow:hidden}
.page--salt{left:30px}
.page--services{left:610px}
.brand{position:absolute;right:26px;top:22px;text-align:right;font-family:"Open Sans",Arial,sans-serif;font-weight:800;font-size:22px;line-height:1.05;color:#3a3a3a;text-transform:uppercase;letter-spacing:.5px;z-index:3}
.photo{position:absolute;background:linear-gradient(160deg,var(--snow-a),var(--snow-b))}
.photo--inset{border:4px solid #fff;box-shadow:0 2px 6px rgba(0,0,0,.25);z-index:2;background:linear-gradient(150deg,#eef2f6,#9aa6b3 70%,var(--machine))}
.swoosh{position:absolute;left:0;width:560px;z-index:2}
.badge-insured{position:absolute;left:18px;top:296px;z-index:4;background:var(--blue);color:#fff;font-family:"Roboto Condensed",Arial,sans-serif;font-weight:700;font-size:24px;line-height:1;text-align:center;padding:8px 16px;border:3px solid #fff;border-radius:6px;transform:rotate(-8deg);box-shadow:0 2px 6px rgba(0,0,0,.3)}
.product-title{position:absolute;top:352px;left:0;width:100%;text-align:center;font-family:"Roboto Condensed",Arial,sans-serif;font-weight:700;font-size:24px;line-height:1.1;color:var(--blue);text-transform:uppercase;z-index:3}
.body-copy{position:absolute;font-size:7.4px;line-height:1.4;color:var(--ink)}
.body-copy p+p{margin-top:5px}
.section-title{font-family:"Roboto Condensed",Arial,sans-serif;font-weight:700;color:var(--blue);text-transform:uppercase;white-space:nowrap}
.ticks{list-style:none}
.ticks li{position:relative;padding-left:12px}
.ticks li::before{content:"";position:absolute;left:0;top:2px;width:7px;height:7px;border:1px solid var(--blue);border-radius:1px}
.ticks li::after{content:"";position:absolute;left:2px;top:2px;width:3px;height:5px;border:solid var(--blue);border-width:0 1.5px 1.5px 0;transform:rotate(40deg)}
.hl{color:var(--blue);font-weight:600}
.footer{position:absolute;left:22px;right:22px;bottom:24px;height:28px;background:var(--blue);border-radius:10px;color:#fff;font-size:8px;display:flex;align-items:center;justify-content:center;gap:6px;white-space:nowrap;padding:0 10px}
.footer .sep{opacity:.7}
.footer svg{width:8px;height:8px;vertical-align:-1px;margin-right:3px}
.hero-title{position:absolute;left:44px;top:196px;font-size:33px;line-height:1.2;color:#111;z-index:3;font-weight:400}
.service-list{font-size:9px;line-height:1.65}
.seals{position:absolute;left:332px;top:568px;width:196px;height:66px;border:1px solid #bbb;border-radius:8px;display:flex;align-items:center;justify-content:space-around;background:#fff}
.seal{width:50px;height:50px}
.company-line{position:absolute;top:648px;left:0;width:100%;text-align:center;font-family:"Roboto Condensed",Arial,sans-serif;font-size:18px;color:var(--blue);text-transform:uppercase}
</style>
</head>
<body>

<section class="page page--salt">
  <div class="photo" style="left:0;top:90px;width:560px;height:240px;background:linear-gradient(170deg,#c9d3dd 0%,#eef2f5 45%,#9aa3ad 100%)" role="img" aria-label="Fleet of white pickup trucks with snow plows on a snowy street"></div>
  <div class="photo photo--inset" style="left:22px;top:14px;width:150px;height:112px" role="img" aria-label="Yellow wheel loader with a snow pusher"></div>
  <div class="brand">Summit Grading<br>&amp; Builders LLC</div>
  <svg class="swoosh" style="top:292px" height="60" viewBox="0 0 560 60" preserveAspectRatio="none">
    <path d="M0 38 C180 10 380 50 560 0 L560 60 L0 60Z" fill="#fff"/>
    <path d="M0 34 C180 6 380 46 560 -4" fill="none" stroke="var(--blue)" stroke-width="6"/>
  </svg>
  <div class="badge-insured">FULLY<br>INSURED</div>
  <h1 class="product-title">Frost Away Magic</h1>

  <div class="body-copy" style="left:26px;top:384px;width:508px">
    <p>Commercial Snow Plowing and Removal is our specialty! With years of experience, a well trained crew and experts in risk mitigation, be assured that Summit Grading And Builders can give the excellent quality service that you expect.</p>
    <p>To properly prepare for our skilled technicians to be at your property with the correct equipment, vehicles and crew, first we must have one of our professionals make an appointment to meet with you and look over the property and to go over what special requirements you might have. During the visit our expert will go over the property's boundaries and map out all the various obstacles, landscaping, walkways and sidewalks, hydrants and other utilities and anything else that might be hidden once the snow start piling up.</p>
  </div>

  <div class="body-copy" style="left:26px;top:464px;width:256px">
    <h2 class="section-title" style="font-size:14px;line-height:1.1;margin-bottom:5px">We only use Frost Away (Magic Salt)</h2>
    <ul class="ticks">
      <li><span class="hl">Frost Away Granular</span> is economically superior. Because it works better and lasts longer, less Frost Away Granular is required to displace an equal amount of ice or snow than with any other ice-melter at any price. Rock salt applications are reduced by 30% to 50%. The need for sand in most circumstances is virtually eliminated.</li>
      <li><span class="hl">Frost Away Granular</span> works faster and lasts longer at much lower temperatures than ordinary rock salt.</li>
      <li><span class="hl">Frost Away Granular</span> has a working temperature of -35°F, whereas regular rock salt is ineffective below 18°F. This is a net 53° degree gain in working temperature, similar to calcium chloride, without the adverse effects. Because of its residual effect, snow and ice will not bond to the pavement. Black ice is virtually eliminated.</li>
      <li><span class="hl">Frost Away Granular</span> is less corrosive. Unlike plain rock</li>
    </ul>
  </div>

  <div class="body-copy" style="left:292px;top:464px;width:244px">
    <h3 style="font-size:8.2px;font-weight:700;margin-bottom:4px">Here is a list of Frost Away Magic Granular features and benefits:</h3>
    <p style="padding-left:12px">salt or calcium chloride, independent tests show Frost Away Magic Granular to be completely less corrosive.</p>
    <ul class="ticks">
      <li><span class="hl">Frost Away Granular</span> will not damage steel doors, thresholds, equipment, carpets, flooring or concrete. In fact, it neutralizes rust!</li>
      <li><span class="hl">Frost Away Granular</span> will not cause concrete to split or any paved surface to degrade in any way. Unlike calcium chloride and ordinary rock salt, Frost Away Granular leaves no visible residue.</li>
      <li>Unlike calcium chloride and ordinary rock salt, Frost Away Granular is safe for people to handle.</li>
      <li><span class="hl">Frost Away Granular</span> is environmentally friendly, releasing far less chlorides into the environment than either plain rock salt or calcium chloride.</li>
      <li><span class="hl">Frost Away Granular</span> is pet safe!</li>
    </ul>
  </div>

  <footer class="footer">
    <span><svg viewBox="0 0 10 10"><path d="M2 1l2 2-1 1.5c.6 1.2 1.3 1.9 2.5 2.5L7 6l2 2-1.5 1.5C4 9 1 6 .5 2.5Z" fill="#fff"/></svg>518-462-3917</span><span class="sep">|</span>
    <span>summitgradingandbuilders@mailbox-example.com</span><span class="sep">|</span>
    <span>www.summitgradingandbuilders-example.com</span>
  </footer>
</section>

<section class="page page--services">
  <div class="photo" style="left:0;top:88px;width:560px;height:250px;background:linear-gradient(160deg,#b9c6d2 0%,#f1f4f7 45%,#d5dbe1 70%,#c7a440 100%)" role="img" aria-label="Large yellow wheel loader pushing snow past pine trees"></div>
  <div class="photo photo--inset" style="left:40px;top:18px;width:172px;height:112px" role="img" aria-label="Compact track loader with a snow pusher"></div>
  <div class="brand">Summit Grading<br>&amp; Builders LLC</div>
  <h1 class="hero-title">Snow Removal<br>Schenectady, NY</h1>
  <svg class="swoosh" style="top:300px" height="50" viewBox="0 0 560 50" preserveAspectRatio="none">
    <path d="M0 40 C200 46 380 30 560 0 L560 50 L0 50Z" fill="#fff"/>
    <path d="M0 36 C200 42 380 26 560 -4" fill="none" stroke="var(--blue)" stroke-width="7"/>
  </svg>

  <div class="body-copy" style="left:28px;top:354px;width:272px;font-size:8.6px;line-height:1.5">
    <p>Winter weather in Upstate New York creates major challenges and safety concerns for commercial property managers. Whether your property <span class="hl">is a retail shopping center,</span> office building, medical/hospital facility, <span class="hl">industrial park, apartment building, or condominium,</span> you need a dependable, responsive partner to quickly and completely clear snow and ice from sidewalks, parking lots, and other walking and driving surfaces.</p>
    <p style="margin-top:10px">Summit Grading And Builders is one of the top commercial snow contractors in the region. We have built a comprehensive system for snow management. Our <span class="hl">earth-friendly deicing techniques</span> are less harmful to the environment and your property.</p>
  </div>

  <div class="photo" style="left:316px;top:356px;width:222px;height:196px;background:linear-gradient(165deg,#e4e9ee 0%,#a9b3bd 55%,#c59d35 100%)" role="img" aria-label="Yellow skid steer clearing snow near bare trees"></div>

  <div style="position:absolute;left:28px;top:524px;width:290px">
    <h2 class="section-title" style="font-size:13px;margin-bottom:3px;text-transform:none">Commercial Snow &amp; Ice Removal Services</h2>
    <ul class="ticks service-list">
      <li>Snow plowing and hauling</li>
      <li>Sidewalk clearing and de-icing</li>
      <li>Pre- and post-storm communication</li>
      <li>Blizzard contingency plans</li>
      <li>Multiple salt storage locations for quicker response</li>
      <li>Dedicated area and route supervisors</li>
      <li>24 hour service</li>
    </ul>
  </div>

  <div class="seals">
    <svg class="seal" viewBox="0 0 50 50"><circle cx="25" cy="25" r="22" fill="#8a8f95"/></svg>
    <svg class="seal" viewBox="0 0 50 50"><path d="M8 4h34v30L25 46 8 34Z" fill="#f08a1e"/></svg>
    <svg class="seal" viewBox="0 0 50 50"><rect x="4" y="8" width="42" height="34" rx="5" fill="#f3a21c"/></svg>
  </div>

  <div class="company-line">Summit Grading And Builders</div>

  <footer class="footer">
    <span><svg viewBox="0 0 10 10"><path d="M2 1l2 2-1 1.5c.6 1.2 1.3 1.9 2.5 2.5L7 6l2 2-1.5 1.5C4 9 1 6 .5 2.5Z" fill="#fff"/></svg>518-462-3917</span><span class="sep">|</span>
    <span>summitgradingandbuilders@mailbox-example.com</span><span class="sep">|</span>
    <span>www.summitgradingandbuilders-example.com</span>
  </footer>
</section>

</body>
</html>
```